Create a bold and border around my logo to make it pop and sign graphic design

I would like someone to create a sign graphic design so I can use on the side of my trucks and put on yard signs. I would to remove a lot of the white and add more of the orange and blue to give it more pop when cars drive past. I would like the services to be removed and for you to leave space for a mobile number that i would add later. I don’t want my logo changed at all. I just want colour and design to be added to the background so i can use it in signage. Same colour as on the sign

```html
<!DOCTYPE html>
<html lang="en">
<head>
<meta charset="utf-8">
<title>Groveworks Sign</title>
<link rel="stylesheet" href="https://fonts.googleapis.com/css2?family=Montserrat:wght@600;700&family=Unbounded:wght@800&display=swap">
<style>
  :root {
    --brand-blue: #3a38c6;
    --brand-orange: #f27405;
    --panel-white: #ffffff;
    --phone-white: #f3f3f3;
    --page-bg: #ececec;
  }
  html, body {
    margin: 0;
    padding: 0;
    width: 1164px;
    height: 1200px;
    overflow: hidden;
    background: var(--page-bg);
  }
  .sign {
    position: absolute;
    left: 42px;
    top: 240px;
    width: 1080px;
    height: 720px;
    display: flex;
    flex-direction: column;
    box-shadow: 0 6px 18px rgba(0,0,0,0.18);
  }
  .band-top-blue { height: 38px; background: var(--brand-blue); }
  .band-top-orange { height: 40px; background: var(--brand-orange); }
  .brand-panel {
    height: 305px;
    background: var(--panel-white);
    display: flex;
    flex-direction: column;
    align-items: center;
    justify-content: center;
    gap: 22px;
  }
  .brand-dot {
    width: 170px;
    height: 170px;
    border-radius: 50%;
    background: var(--brand-orange);
  }
  .brand-name {
    font-family: "Montserrat", sans-serif;
    font-weight: 700;
    font-size: 54px;
    letter-spacing: 1px;
    color: var(--brand-blue);
    line-height: 1;
  }
  .phone-panel {
    height: 259px;
    background: var(--brand-orange);
    display: flex;
    align-items: center;
    justify-content: center;
  }
  .phone-number {
    font-family: "Unbounded", sans-serif;
    font-weight: 800;
    font-size: 100px;
    color: var(--phone-white);
    letter-spacing: -2px;
    line-height: 1;
  }
  .web-band {
    height: 78px;
    background: var(--brand-blue);
    display: flex;
    align-items: center;
    justify-content: center;
  }
  .web-address {
    font-family: "Montserrat", sans-serif;
    font-weight: 600;
    font-size: 24px;
    letter-spacing: 12px;
    color: var(--phone-white);
  }
</style>
</head>
<body>
  <div class="sign">
    <div class="band-top-blue"></div>
    <div class="band-top-orange"></div>
    <div class="brand-panel">
      <div class="brand-dot"></div>
      <div class="brand-name">GROVEWORKS</div>
    </div>
    <div class="phone-panel">
      <div class="phone-number">123-456-7890</div>
    </div>
    <div class="web-band">
      <div class="web-address">www.groveworks.nz</div>
    </div>
  </div>
</body>
</html>
```